Business Card and Stationary Design for Solstice Land Company
Solstice Land Partners
Business Card and Stationary Design for Solstice Land Company - Real Estate
Creative Brief
Use same font as used in my logo
Tobias "TK" Kalder
Realtor
2876 Mellow Crest Lane Irvine, CA 92611
tk@TheSolsticeLP.example
www.TheSolsticeLP.example
BRE Lic: 07326159
We need the following design work done: Business Cards, Presentation Folder, Letterhead, Envelopes. We will upload our logo and the design templates from our print shop for all the above items needed in order to print correctly. Business Cards (Front & Back): 4 color both sides. Presentation Folder - (Front, Back and inside) 4 colors all sides, including business card slit inside.
We will upload pictures of sample business cards (Front and Back) that we like from competitor companies.

```html
<!DOCTYPE html>
<html lang="en">
<head>
<meta charset="utf-8">
<title>Solstice Land Partners – Business Card</title>
<link href="https://fonts.googleapis.com/css2?family=Montserrat:wght@400;600;800&display=swap" rel="stylesheet">
<style>
  :root {
    --backdrop: #e6e6e6;
    --card-white: #ffffff;
    --ink: #1f1f1f;
    --ink-soft: #555555;
    --brand-orange: #f26b0f;
    --band-black: #111111;
    --on-dark: #f2f2f2;
  }
  html, body {
    margin: 0;
    width: 1200px;
    height: 670px;
    overflow: hidden;
    background: var(--backdrop);
    font-family: "Montserrat", Arial, sans-serif;
  }
  .sheet {
    position: relative;
    width: 1200px;
    height: 670px;
  }
  .card {
    position: absolute;
    top: 180px;
    width: 540px;
    height: 309px;
    background: var(--card-white);
    box-shadow: 0 6px 18px rgba(0,0,0,0.18);
    overflow: hidden;
  }
  .card--front { left: 40px; }
  .card--back { left: 620px; }

  .brand {
    position: absolute;
    display: flex;
    align-items: center;
    gap: 8px;
    color: var(--ink);
    font-weight: 800;
    white-space: nowrap;
  }
  .brand__square {
    width: 22px;
    height: 22px;
    background: var(--brand-orange);
  }
  .card--front .brand {
    left: 50%;
    top: 118px;
    transform: translateX(-50%);
    font-size: 26px;
  }
  .card--back .brand {
    left: 34px;
    top: 56px;
    font-size: 19px;
    gap: 7px;
  }
  .card--back .brand__square {
    width: 18px;
    height: 18px;
  }

  .wave {
    position: absolute;
    inset: 0;
    width: 540px;
    height: 309px;
  }
  .wave__orange { fill: var(--brand-orange); }
  .wave__black { fill: var(--band-black); }

  .holder {
    position: absolute;
    left: 40px;
    top: 206px;
  }
  .holder__name {
    margin: 0;
    font-size: 13px;
    font-weight: 600;
    letter-spacing: 0.5px;
    text-transform: uppercase;
    color: var(--ink);
  }
  .holder__role {
    margin: 3px 0 0;
    font-size: 10px;
    color: var(--ink-soft);
  }

  .contact {
    position: absolute;
    left: 408px;
    top: 40px;
    margin: 0;
    padding: 0;
    list-style: none;
    color: var(--on-dark);
    font-size: 8px;
    line-height: 1.4;
  }
  .contact__group { margin-bottom: 12px; }
  .contact__item { display: flex; align-items: center; gap: 5px; }
  .contact__icon { width: 8px; height: 8px; fill: var(--brand-orange); }
</style>
</head>
<body>
<main class="sheet">
  <section class="card card--front" aria-label="Business card front">
    <div class="brand"><span class="brand__square"></span>Solstice Land Partners</div>
  </section>

  <section class="card card--back" aria-label="Business card back">
    <svg class="wave" viewBox="0 0 540 309" aria-hidden="true">
      <path class="wave__orange" d="M0,258 C150,258 262,250 310,190 C352,136 346,28 392,0 L540,0 L540,309 L0,309 Z"/>
      <path class="wave__black" d="M0,268 C156,268 272,258 320,198 C362,144 358,36 404,0 L540,0 L540,309 L0,309 Z"/>
    </svg>

    <div class="brand"><span class="brand__square"></span>Solstice Land Partners</div>

    <div class="holder">
      <p class="holder__name">Tobias "TK" Kalder</p>
      <p class="holder__role">Managing Director</p>
    </div>

    <ul class="contact">
      <li class="contact__group">
        <div class="contact__item">2876 Mellow Crest Lane</div>
        <div class="contact__item">Irvine, CA 92611</div>
      </li>
      <li class="contact__group">
        <div class="contact__item"><svg class="contact__icon" viewBox="0 0 10 10"><path d="M2 0h2l1 3-1.5 1a6 6 0 0 0 2.5 2.5L7 5l3 1v2a2 2 0 0 1-2 2A8 8 0 0 1 0 2a2 2 0 0 1 2-2z"/></svg>714.555.0142</div>
        <div class="contact__item"><svg class="contact__icon" viewBox="0 0 10 10"><path d="M2 0h2l1 3-1.5 1a6 6 0 0 0 2.5 2.5L7 5l3 1v2a2 2 0 0 1-2 2A8 8 0 0 1 0 2a2 2 0 0 1 2-2z"/></svg>714.555.0187</div>
        <div class="contact__item"><svg class="contact__icon" viewBox="0 0 10 10"><path d="M2 0h2l1 3-1.5 1a6 6 0 0 0 2.5 2.5L7 5l3 1v2a2 2 0 0 1-2 2A8 8 0 0 1 0 2a2 2 0 0 1 2-2z"/></svg>714.555.0163</div>
      </li>
      <li class="contact__group">
        <div class="contact__item">tk@TheSolsticeLP.example</div>
        <div class="contact__item">www.TheSolsticeLP.example</div>
      </li>
    </ul>
  </section>
</main>
</body>
</html>
```